Vireo Imaging - Diagnostic Ultrasound Flyer

About US
Vireo Imaging is a concierge ultrasound company that provides onsite or offsite diagnostic ultrasounds. We have over 14 years experience in sonography, business management, and customer service. We offer both the physician and patient flexibility, convenience, and access to timely services.

We provide ultrasounds for the following specialties:
Obstetrics/Gynecology
Abdominal
Small Parts
Vascular

Company Features:
1. Onsite or Offsite Scans
2. Images Available Immediately for Referring Physician and Patient
3. Flexible Options for Ultrasound Interpretation/Billing
4. Access to Interpreting Radiologist
5. Final Report Process - 1-2 Business Days/ 1 hour for STAT.
6. PACS Storage with Secure Access.

We need a place to add in our contact information (address, email, website, phone)

We already have a logo and would like to use it ( they are attached). We would the colors to match the logo colors....maybe lighter version of yellow and blue.

```html
<!DOCTYPE html>
<html lang="en">
<head>
<meta charset="utf-8">
<title>Vireo Imaging – Diagnostic Ultrasound Flyer</title>
<link rel="stylesheet" href="https://fonts.googleapis.com/css2?family=Anton&family=Arimo:wght@400;700&family=Montserrat:wght@300;400;800;900&display=swap">
<style>
  :root{
    --navy:#1c1ca8;
    --gold:#fbbd2d;
    --lavender:#c6c6f8;
    --cream:#f9e8c6;
    --pill:#fff4dc;
    --ink:#2c2c3a;
    --page:#f1f1f3;
  }
  *{margin:0;padding:0;box-sizing:border-box;}
  html,body{width:1200px;height:2602px;overflow:hidden;background:var(--page);}
  .flyer{
    position:absolute;left:50px;top:588px;width:822px;height:1065px;
    transform:scale(1.3382);transform-origin:0 0;
    background:#fff;overflow:hidden;
    box-shadow:0 4px 14px rgba(0,0,0,.18);
    font-family:"Arimo",Arial,sans-serif;color:var(--ink);
  }
  .flyer-shapes{position:absolute;inset:0;width:822px;height:1065px;}
  .abs{position:absolute;}
  .brand{left:45px;top:46px;font-family:"Montserrat",sans-serif;font-weight:400;font-size:30px;line-height:36px;color:var(--navy);letter-spacing:.5px;}
  .title{font-family:"Anton",sans-serif;font-size:48px;line-height:48px;letter-spacing:2px;font-weight:400;transform:scaleX(1.12);transform-origin:0 0;white-space:nowrap;}
  .title-top{left:44px;top:125px;color:var(--navy);}
  .title-bottom{left:48px;top:184px;color:var(--gold);}
  .heading{font-family:"Montserrat",sans-serif;font-size:16px;color:#111;letter-spacing:1px;text-transform:uppercase;}
  .heading b{font-weight:800;}
  .heading span{font-weight:300;}
  .heading::after{content:"";position:absolute;left:0;bottom:-7px;width:36px;height:2px;background:#111;}
  .about-heading{left:45px;top:318px;}
  .about-text{left:45px;top:360px;width:400px;font-size:10.6px;line-height:14.8px;color:#444;}
  .about-text b{color:#222;}
  .specialty-heading{left:45px;top:444px;font-size:15px;line-height:20px;}
  .specialty-heading::after{bottom:-10px;}
  .offer-heading{left:495px;top:318px;}
  .offer-box{left:470px;top:363px;width:352px;height:125px;background:var(--gold);}
  .offer-divider{left:622px;top:378px;width:1px;height:100px;background:#fff;opacity:.8;}
  .offer-item{display:flex;align-items:center;}
  .offer-icon{width:26px;height:26px;border-radius:50%;background:var(--navy);border:2px solid #fff;flex:none;position:relative;z-index:1;}
  .offer-label{background:var(--pill);font-size:11.5px;color:var(--navy);padding:4px 8px 4px 14px;margin-left:-6px;line-height:14px;}
  .spec-block{left:0;top:507px;width:45px;height:60px;background:var(--navy);}
  .spec-frame{left:45px;top:507px;width:652px;height:60px;border:1px solid var(--navy);background:#fff;}
  .spec-item{top:525px;display:flex;align-items:center;gap:10px;font-size:12px;color:#222;}
  .spec-icon{width:22px;height:22px;border-radius:4px;background:var(--navy);}
  .spec-label{background:#f0f0f4;padding:2px 12px 2px 2px;}
  .spec-sep{top:517px;width:1px;height:40px;background:#9a9ac8;}
  .features-heading{left:0;width:822px;top:604px;text-align:center;font-family:"Montserrat",sans-serif;font-size:15px;letter-spacing:1px;color:#111;text-transform:uppercase;}
  .features-heading b{font-weight:800;}
  .features-heading span{font-weight:300;}
  .features-rule{left:300px;top:630px;width:220px;height:1px;background:#333;}
  .features-rule-bold{left:393px;top:629px;width:36px;height:3px;background:#111;}
  .feature-photo{width:136px;height:90px;border:1.5px solid var(--navy);}
  .feature-caption{width:170px;text-align:center;font-size:10.8px;line-height:14.5px;color:#333;}
  .contact-title{left:45px;top:998px;font-family:"Montserrat",sans-serif;font-size:10px;font-weight:800;color:#111;}
  .contact-title span{font-weight:400;}
  .contact-title::after{content:"";position:absolute;left:0;bottom:-3px;width:60px;height:1px;background:#111;}
  .contact-line{display:flex;align-items:center;gap:6px;font-size:10px;color:#222;white-space:nowrap;}
  .contact-line svg{width:10px;height:10px;fill:var(--navy);flex:none;}
  .phone{font-weight:700;}
  .web b{color:var(--navy);font-weight:400;}
</style>
</head>
<body>
<main class="flyer">
  <svg class="flyer-shapes" viewBox="0 0 822 1065">
    <defs>
      <linearGradient id="machineTone" x1="0" y1="0" x2="0.4" y2="1">
        <stop offset="0" stop-color="#f0553f"/>
        <stop offset="0.3" stop-color="#e9c7cf"/>
        <stop offset="0.65" stop-color="#e4e5ec"/>
        <stop offset="1" stop-color="#cfd1da"/>
      </linearGradient>
      <linearGradient id="scanTone" x1="0" y1="0" x2="1" y2="1">
        <stop offset="0" stop-color="#d8def0"/>
        <stop offset="0.45" stop-color="#8ea2d4"/>
        <stop offset="0.75" stop-color="#e9e9f2"/>
        <stop offset="1" stop-color="#5d74b8"/>
      </linearGradient>
    </defs>
    <polygon points="0,0 142,0 132,14 0,14" fill="var(--gold)"/>
    <polygon points="142,0 822,0 822,12 132,14" fill="var(--lavender)"/>
    <polygon points="420,12 480,12 300,262 238,262" fill="var(--lavender)"/>
    <polygon points="0,240 300,240 262,292 0,292" fill="var(--cream)"/>
    <polygon points="0,205 30,178 0,240" fill="var(--lavender)"/>
    <polygon points="35,178 392,178 345,240 0,240" fill="var(--navy)"/>
    <polygon points="455,0 822,0 822,262 300,262" fill="url(#machineTone)" role="img" aria-label="Photo of an ultrasound machine control panel"/>
    <polygon points="822,215 822,262 785,262" fill="var(--cream)"/>
    <polygon points="300,250 312,250 274,292 262,292" fill="var(--navy)"/>
    <rect x="262" y="281" width="560" height="11" fill="var(--navy)"/>
    <polygon points="43,587 777,587 777,830 490,830 430,980 43,980" fill="var(--lavender)"/>
    <polygon points="455,835 822,818 822,1065 420,1065" fill="url(#scanTone)" role="img" aria-label="Collage of ultrasound equipment and a patient receiving a scan"/>
    <polygon points="0,1052 445,1052 435,1065 0,1065" fill="var(--navy)"/>
  </svg>

  <div class="abs brand">Vireo Imaging</div>
  <h1 class="abs title title-top">DIAGNOSTIC</h1>
  <h1 class="abs title title-bottom">ULTRASOUND</h1>

  <h2 class="abs heading about-heading"><b>About</b> <span>Us</span></h2>
  <p class="abs about-text"><b>Vireo Imaging</b> is a concierge ultrasound company that provides onsite or offsite diagnostic ultrasounds. We have over 14 years experience in sonography, business management, and customer service.</p>

  <h2 class="abs heading specialty-heading"><b>We provide ultrasounds</b><br><span>For the following specialties:</span></h2>

  <h2 class="abs heading offer-heading"><b>We</b> <span>Offer</span></h2>
  <div class="abs offer-box"></div>
  <div class="abs offer-divider"></div>
  <div class="abs offer-item" style="left:490px;top:379px;"><span class="offer-icon"></span><span class="offer-label" style="width:98px;">Physician</span></div>
  <div class="abs offer-item" style="left:490px;top:414px;"><span class="offer-icon"></span><span class="offer-label" style="width:98px;">Flexibility</span></div>
  <div class="abs offer-item" style="left:490px;top:449px;"><span class="offer-icon"></span><span class="offer-label" style="width:98px;">Patient</span></div>
  <div class="abs offer-item" style="left:638px;top:378px;"><span class="offer-icon"></span><span class="offer-label" style="width:116px;">Convenience</span></div>
  <div class="abs offer-item" style="left:638px;top:414px;"><span class="offer-icon"></span><span class="offer-label" style="width:116px;">Access to<br>timely services</span></div>

  <div class="abs spec-block"></div>
  <div class="abs spec-frame"></div>
  <div class="abs spec-item" style="left:62px;"><span class="spec-icon"></span><span class="spec-label">Obstetrics/Gynecology</span></div>
  <div class="abs spec-sep" style="left:267px;"></div>
  <div class="abs spec-item" style="left:285px;"><span class="spec-icon"></span><span class="spec-label">Abdominal</span></div>
  <div class="abs spec-sep" style="left:413px;"></div>
  <div class="abs spec-item" style="left:428px;"><span class="spec-icon"></span><span class="spec-label">Small Parts</span></div>
  <div class="abs spec-sep" style="left:557px;"></div>
  <div class="abs spec-item" style="left:572px;"><span class="spec-icon"></span><span class="spec-label">Vascular</span></div>

  <h2 class="abs features-heading"><b>Company</b> <span>Features:</span></h2>
  <div class="abs features-rule"></div>
  <div class="abs features-rule-bold"></div>

  <div class="abs feature-photo" style="left:78px;top:653px;background:linear-gradient(135deg,#c9b39c,#eef0f2 55%,#7f93a8);" role="img" aria-label="Photo of a sonographer at an ultrasound keyboard"></div>
  <p class="abs feature-caption" style="left:61px;top:763px;">Onsite or<br>Offsite Scans</p>
  <div class="abs feature-photo" style="left:253px;top:653px;background:linear-gradient(135deg,#f3e4d8,#e4b89c 55%,#f1ece8);" role="img" aria-label="Photo of clasped hands of physician and patient"></div>
  <p class="abs feature-caption" style="left:236px;top:754px;">Images Available<br>Immediately for Referring<br>Physician and Patient</p>
  <div class="abs feature-photo" style="left:430px;top:653px;background:linear-gradient(135deg,#2e3f4f,#6a8b98 50%,#c9d4d8);" role="img" aria-label="Photo of an ultrasound scan on a monitor"></div>
  <p class="abs feature-caption" style="left:413px;top:754px;">Flexible Options for<br>Ultrasound Interpretation<br>/Billing</p>
  <div class="abs feature-photo" style="left:607px;top:653px;background:linear-gradient(135deg,#eef0f4,#b9c2cf 55%,#56627a);" role="img" aria-label="Photo of a radiologist reviewing a scan with a patient"></div>
  <p class="abs feature-caption" style="left:590px;top:763px;">Access to Interpreting<br>Radiologist</p>

  <div class="abs feature-photo" style="left:78px;top:815px;background:linear-gradient(135deg,#e8ecef,#7ea0c4 50%,#2b4c8c);" role="img" aria-label="Photo of a gloved hand operating ultrasound equipment"></div>
  <p class="abs feature-caption" style="left:61px;top:917px;">Onsite or Offsite Final Report<br>Process - 1-2 Business Days/<br>1 hour for STAT. Scans</p>
  <div class="abs feature-photo" style="left:253px;top:815px;background:linear-gradient(135deg,#0f2c4a,#2b6f9c 55%,#d9cfc6);" role="img" aria-label="Photo of a laptop showing a secure access screen"></div>
  <p class="abs feature-caption" style="left:236px;top:917px;">PACS Storage with<br>Secure Access.</p>

  <h3 class="abs contact-title">Contact <span>Us</span></h3>
  <div class="abs contact-line phone" style="left:45px;top:1016px;">
    <svg viewBox="0 0 10 10"><path d="M2 0.5 L3.6 2.6 L2.8 3.6 C3.4 5 5 6.6 6.4 7.2 L7.4 6.4 L9.5 8 L8.4 9.5 C4.6 9.2 0.8 5.4 0.5 1.6 Z"/></svg>555-0142-370
  </div>
  <div class="abs contact-line" style="left:155px;top:1000px;">
    <svg viewBox="0 0 10 10"><path d="M5 0 C2.8 0 1.4 1.6 1.4 3.5 C1.4 6 5 10 5 10 C5 10 8.6 6 8.6 3.5 C8.6 1.6 7.2 0 5 0 Z M5 2.2 A1.4 1.4 0 1 1 5 5 A1.4 1.4 0 1 1 5 2.2 Z"/></svg>your address, City, State goes here
  </div>
  <div class="abs contact-line" style="left:155px;top:1016px;">
    <svg viewBox="0 0 10 10"><path d="M0.5 2 H9.5 V8.5 H0.5 Z M0.8 2.4 L5 5.6 L9.2 2.4" stroke="#fff" stroke-width="0.7"/></svg>info@vireo-imaging.com
  </div>
  <div class="abs contact-line web" style="left:283px;top:1016px;">
    <svg viewBox="0 0 10 10"><circle cx="5" cy="5" r="4.3" fill="none" stroke="var(--navy)" stroke-width="1"/><ellipse cx="5" cy="5" rx="1.8" ry="4.3" fill="none" stroke="var(--navy)" stroke-width="0.8"/><path d="M0.8 5 H9.2" stroke="var(--navy)" stroke-width="0.8"/></svg><span>www.<b>VIREOIMAGING</b>.com</span>
  </div>
</main>
</body>
</html>
```